Vantolle Car Wrap

Car wrap for a white 2019 Koravi Dart
Vantolle Group - Real Estate Agency

Logos, Futura Font & colour guide attached

Target Market(s)

Real Estate

Industry/Entity Type

Real Estate

Requirements
Must have
• Must have wording:
• All things real estate
• Buy
• Sell
• Rent
• www.vantolle.com.au
• Phone: 07 3829 5174

```html
<!DOCTYPE html>
<html lang="en">
<head>
<meta charset="utf-8">
<title>Vantolle Group – Car Wrap Side Panel</title>
<link rel="stylesheet" href="https://fonts.googleapis.com/css2?family=Jost:wght@400;500;600;700&display=swap">
<style>
  :root {
    --wrap-white: #ffffff;
    --brand-purple: #2b1a63;
    --brand-purple-deep: #1f1250;
    --brand-orange: #e8891c;
    --text-grey: #8b8b8b;
    --icon-grey: #9a9a9a;
    --canvas-bg: #ffffff;
  }
  * { margin: 0; padding: 0; box-sizing: border-box; }
  html, body {
    width: 1200px;
    height: 1200px;
    overflow: hidden;
    background: var(--canvas-bg);
  }
  .wrap-canvas {
    position: relative;
    width: 1200px;
    height: 1200px;
    font-family: "Jost", "Futura", sans-serif;
  }
  .wrap-graphics {
    position: absolute;
    left: 0;
    top: 0;
  }
  .tagline-block {
    position: absolute;
    left: 397px;
    top: 614px;
    line-height: 1.15;
  }
  .tagline-main {
    font-weight: 600;
    font-size: 18px;
    letter-spacing: 0.5px;
    color: var(--text-grey);
    text-transform: uppercase;
  }
  .tagline-services {
    font-weight: 600;
    font-size: 15px;
    color: var(--brand-orange);
    margin-top: 3px;
  }
  .slogan {
    position: absolute;
    left: 633px;
    top: 626px;
    font-weight: 600;
    font-size: 12px;
    line-height: 1.2;
    color: var(--brand-orange);
    white-space: nowrap;
  }
  .brand-name {
    position: absolute;
    left: 572px;
    top: 649px;
    font-weight: 400;
    font-size: 60px;
    line-height: 1;
    color: var(--brand-purple);
    white-space: nowrap;
  }
  .brand-descriptor {
    position: absolute;
    left: 649px;
    top: 710px;
    font-weight: 400;
    font-size: 11px;
    letter-spacing: 8px;
    color: var(--text-grey);
  }
  .social-block {
    position: absolute;
    left: 787px;
    top: 644px;
  }
  .social-square {
    display: block;
    width: 11px;
    height: 11px;
    background: var(--icon-grey);
    border-radius: 1px;
    margin-bottom: 6px;
  }
  .social-handle {
    display: block;
    font-size: 6px;
    color: var(--icon-grey);
    margin-left: -6px;
  }
  .contact-line {
    position: absolute;
    display: flex;
    align-items: center;
    gap: 8px;
    font-weight: 600;
    color: var(--wrap-white);
    white-space: nowrap;
  }
  .contact-phone { left: 405px; top: 735px; font-size: 14px; letter-spacing: 1.8px; }
  .contact-web { left: 560px; top: 741px; font-size: 13px; letter-spacing: 0.6px; }
  .contact-icon { width: 16px; height: 16px; flex: none; }
</style>
</head>
<body>
<main class="wrap-canvas">
  <svg class="wrap-graphics" width="1200" height="1200" viewBox="0 0 1200 1200">
    <path class="swoosh-band" fill="var(--brand-purple)"
      d="M187 700
         C 215 690, 250 676, 272 668
         L 356 664
         C 372 690, 392 712, 430 724
         C 480 734, 540 732, 600 731
         L 775 729
         L 775 772
         L 400 770
         C 300 768, 230 764, 187 756 Z"/>
    <path class="swoosh-highlight" fill="none" stroke="#4a3a8a" stroke-width="1.5"
      d="M272 686 C 320 700, 370 726, 430 734 C 500 742, 600 740, 775 738"/>
    <rect class="rooftop-illustration" role="img"
      aria-label="Illustration: silhouette of houses and trees on a hill with a winding orange path"
      x="268" y="628" width="90" height="52" fill="var(--brand-purple-deep)"/>
  </svg>

  <div class="tagline-block">
    <div class="tagline-main">All Things</div>
    <div class="tagline-main">Real Estate</div>
    <div class="tagline-services">Buy · Sell · Rent</div>
  </div>

  <div class="slogan">Let us show you property</div>

  <div class="brand-name">vantolle</div>
  <div class="brand-descriptor">GROUP</div>

  <div class="social-block">
    <span class="social-square"></span>
    <span class="social-square"></span>
    <span class="social-handle">/vantolle</span>
  </div>

  <div class="contact-line contact-phone">
    <svg class="contact-icon" viewBox="0 0 16 16" aria-hidden="true">
      <circle cx="8" cy="8" r="8" fill="var(--brand-orange)"/>
      <path d="M5.2 4.2l1.4-.3.8 2-1 .8c.5 1.1 1.3 1.9 2.4 2.4l.8-1 2 .8-.3 1.4c-3.3.2-6.3-2.8-6.1-6.1z" fill="var(--brand-purple)"/>
    </svg>
    <span>07 3829 5174</span>
  </div>

  <div class="contact-line contact-web">
    <svg class="contact-icon" viewBox="0 0 16 16" aria-hidden="true">
      <g fill="none" stroke="var(--brand-orange)" stroke-width="1.2">
        <circle cx="8" cy="8" r="6.5"/>
        <ellipse cx="8" cy="8" rx="3" ry="6.5"/>
        <line x1="1.5" y1="8" x2="14.5" y2="8"/>
        <line x1="2.5" y1="4.8" x2="13.5" y2="4.8"/>
        <line x1="2.5" y1="11.2" x2="13.5" y2="11.2"/>
      </g>
    </svg>
    <span>WWW.VANTOLLE.COM.AU</span>
  </div>
</main>
</body>
</html>
```